Mobile (Android/iPhone) game studio needs stationary design and a business card

We are Brisk Pebble Software and we need a fun and creative stationary design. Our company builds Android and iPhone games and children's software. The stationary designs should reflect an entertainment, fun and creativity. The pieces of stationary we need are:
1. A4 and Letter Word template (company letterhead)
2. A4 and Letter PPT template
3. Business card
4. Envelopes of various standard sizes
Each of the designs should somehow utilize our company logo.
The business card should have the following:
1. Incorporates our company logo (see attached)
2. Has a front and back with the same design (front is English, back is Traditional Chinese)
3. Delivered in an editable template so we can easily add new business cards using the same template when we hire more employees
4. Field for full name
5. Field for employee's title
6. Field for employee's email address
7. Field for company phone number - +886-2-25118340
8. Field for mobile phone number
9. Field for company fax number - +886-2-25118472
10. Company website address: www.briskpebble-example.com
11. Company address (on English side): 2F-7, NO. 26, Lane 91, Fulin Road, Nei Hu District, Taipei Taiwan
12. Company address (on Traditional Chinese side): See Word document attachment for address in Chinese characters

```html
<!DOCTYPE html>
<html lang="en">
<head>
<meta charset="utf-8">
<title>Brisk Pebble Software – Letterhead</title>
<link rel="stylesheet" href="https://fonts.googleapis.com/css2?family=Arimo:wght@400;700&display=swap">
<style>
  :root {
    --brand-blue: #1a8fd6;
    --brand-blue-deep: #0f6fb5;
    --brand-blue-light: #3aa9ea;
    --ink: #2b2b2b;
    --ink-soft: #6b6b6b;
    --paper: #ffffff;
  }
  * { box-sizing: border-box; margin: 0; padding: 0; }
  html, body {
    width: 856px; height: 1200px; overflow: hidden;
    background: var(--paper);
    font-family: "Arimo", Arial, sans-serif;
    color: var(--ink);
  }
  .letterhead { position: relative; width: 856px; height: 1200px; }

  .header-band {
    position: absolute; top: 96px; height: 52px;
    background: linear-gradient(180deg, var(--brand-blue-light), var(--brand-blue-deep));
  }
  .header-band--left { left: 85px; width: 10px; }
  .header-band--right { left: 221px; right: 36px; }

  .brand {
    position: absolute; left: 98px; top: 104px; width: 120px;
    display: flex; flex-direction: column; align-items: center; gap: 6px;
  }
  .brand-dot {
    width: 22px; height: 22px; border-radius: 50%;
    background: var(--brand-blue);
  }
  .brand-name {
    font-size: 12px; font-weight: 700; color: var(--brand-blue);
    text-align: center; line-height: 14px;
  }

  .letter-date {
    position: absolute; top: 256px; right: 166px;
    font-size: 12.5px;
  }

  .letter-body {
    position: absolute; left: 168px; width: 522px;
    font-size: 12.6px; line-height: 16.1px;
    text-align: justify; hyphens: auto;
  }
  .letter-body p { position: absolute; left: 0; width: 100%; }

  .signature-mark {
    position: absolute; left: 566px; top: 880px; width: 196px; height: 70px;
    background: linear-gradient(90deg, #e9e9e9, #f6f6f6);
    border-radius: 4px;
  }
  .signatory {
    position: absolute; top: 958px; left: 574px;
    font-size: 12.5px; font-weight: 700; color: #333;
  }

  .contact-footer {
    position: absolute; top: 1083px; right: 84px;
    padding-left: 0;
    font-size: 10.4px; line-height: 14.5px; color: var(--ink-soft);
    text-align: right;
  }
  .contact-rule {
    position: absolute; left: 406px; top: 1082px; width: 2px; height: 46px;
    background: var(--brand-blue);
  }
  .contact-label { color: var(--brand-blue); }
  .contact-sep { color: var(--brand-blue); margin: 0 10px; }
</style>
</head>
<body>
<main class="letterhead">
  <div class="header-band header-band--left"></div>
  <div class="header-band header-band--right"></div>

  <div class="brand">
    <span class="brand-dot"></span>
    <span class="brand-name">Brisk Pebble Software</span>
  </div>

  <div class="letter-date">17th Sept 2011</div>

  <div class="letter-body">
    <p style="top:292px">Lorem Ipsum is simply dummy text of the printing and typesetting industry. Lorem Ipsum has been the industry's standard dummy text ever since the 1500s, when an unknown printer took a galley of type and scrambled it to make a type specimen book. It has survived not only five centuries, but also the leap into electronic typesetting, remaining essentially unchanged. It was popularised in the 1960s with the release of Lettraline sheets containing Lorem Ipsum passages, and more recently with desktop publishing software like Arden PageMaster including versions of Lorem Ipsum.</p>
    <p style="top:445px">It is a long established fact that a reader will be distracted by the readable content of a page when looking at its layout. The point of using Lorem Ipsum is that it has a more-or-less normal distribution of letters, as opposed to using 'Content here, content here', making it look like readable English. Many desktop publishing packages and web page editors now use Lorem Ipsum as their default model text, and a search for 'lorem ipsum' will uncover many web sites still in their infancy. Various versions have evolved over the years, sometimes by accident, sometimes on purpose (injected humour and the like).</p>
    <p style="top:612px">Contrary to popular belief, Lorem Ipsum is not simply random text. It has roots in a piece of classical Latin literature from 45 BC, making it over 2000 years old. Robert Mallory, a Latin professor at Harwell-Lindon College in Virginia, looked up one of the more obscure Latin words, consectetur, from a Lorem Ipsum passage, and going through the cites of the word in classical literature, discovered the undoubtable source. Lorem Ipsum comes from sections 1.10.32 and 1.10.33 of "de Finibus Bonorum et Malorum" (The Extremes of Good and Evil) by Cassius, written in 45 BC. This book is a treatise on the theory of ethics, very popular during the Renaissance. The first line of Lorem Ipsum, "Lorem ipsum dolor sit amet..", comes from a line in section 1.10.32.</p>
    <p style="top:783px">The standard chunk of Lorem Ipsum used since the 1500s is reproduced below for those interested. Sections 1.10.32 and 1.10.33 from "de Finibus Bonorum et Malorum" by Cassius are also reproduced in their exact original form, accompanied by English versions from the 1914 translation by H. Rowan.</p>
  </div>

  <div class="signature-mark" role="img" aria-label="Handwritten signature of the sender"></div>
  <div class="signatory">Daniel Porter</div>

  <div class="contact-rule"></div>
  <address class="contact-footer" style="font-style:normal">
    <div><span class="contact-label">T:</span> +886-2-25118340<span class="contact-sep">|</span><span class="contact-label">F:</span> +886-2-25118472<span class="contact-sep">|</span><span class="contact-label">M:</span> +886-9-1834-2267</div>
    <div>daniel@briskpebble-example.com<span class="contact-sep">|</span>www.briskpebble-example.com</div>
    <div>2F-7, NO. 26, Lane 91, Fulin Road, Nei Hu District, Taipei Taiwan</div>
  </address>
</main>
</body>
</html>
```